Banner ad template

Replace banners on our website with clean, compelling design to promote our wholesale company. As we sell to retailers, audience on our website need to be compelled by these banners that radiate trust and need to be convincing in order to push customer to place an orders online. I added some examples below. Please make it as amazing looking possible

```html
<!DOCTYPE html>
<html lang="en">
<head>
<meta charset="utf-8">
<title>Smartphone Accessories Cover</title>
<link rel="stylesheet" href="https://fonts.googleapis.com/css2?family=Fira+Sans+Condensed:wght@800&family=Fira+Sans+Extra+Condensed:wght@800&family=Roboto:wght@500&display=swap">
<style>
  :root {
    --page-bg: #e9ebef;
    --banner-blue: #1a55d6;
    --banner-mid: #1d8fd8;
    --banner-teal: #0fd6c6;
    --headline-yellow: #fff200;
    --headline-shadow: rgba(10, 30, 80, 0.55);
    --product-light: rgba(225, 240, 250, 0.75);
    --product-shade: rgba(150, 190, 220, 0.55);
    --display-light: rgba(235, 245, 250, 0.85);
    --display-shade: rgba(170, 200, 215, 0.7);
    --avatar-fill: #0f6a99;
    --white: #ffffff;
    --button-text: #2f3033;
    --button-border: #ccd0d5;
    --tab-active: #4b4f56;
    --tab-link: #4a67a6;
    --tab-divider: #e3e5e9;
  }
  * { box-sizing: border-box; margin: 0; padding: 0; }
  html, body {
    width: 1200px;
    height: 960px;
    overflow: hidden;
    background: var(--page-bg);
  }
  .profile-header {
    position: absolute;
    left: 67px;
    top: 253px;
    width: 1066px;
    height: 446px;
    background: var(--white);
    box-shadow: 0 6px 24px rgba(40, 50, 70, 0.22);
  }
  .cover {
    position: absolute;
    left: 0;
    top: 0;
    width: 1066px;
    height: 394px;
    overflow: hidden;
    background:
      radial-gradient(ellipse 420px 260px at 42% 62%, rgba(60, 110, 230, 0.55), transparent 70%),
      linear-gradient(100deg, var(--banner-blue) 0%, var(--banner-mid) 48%, var(--banner-teal) 100%);
  }
  .headline {
    position: absolute;
    left: 97px;
    top: 66px;
    width: 772px;
    color: var(--headline-yellow);
    text-transform: uppercase;
    text-shadow: 2px 3px 4px var(--headline-shadow);
    text-align: center;
  }
  .headline-main {
    display: block;
    font-family: "Fira Sans Condensed", sans-serif;
    font-weight: 800;
    font-size: 64px;
    line-height: 1;
    white-space: nowrap;
  }
  .headline-sub {
    display: block;
    margin-top: 8px;
    font-family: "Fira Sans Extra Condensed", sans-serif;
    font-weight: 800;
    font-size: 50px;
    line-height: 1;
    white-space: nowrap;
  }
  .product-row {
    position: absolute;
    left: 228px;
    top: 257px;
    width: 660px;
    height: 82px;
    display: flex;
    justify-content: space-between;
    align-items: flex-end;
  }
  .product {
    width: 86px;
    height: 76px;
    border-radius: 6px;
    background: linear-gradient(160deg, var(--product-light), var(--product-shade));
  }
  .display-stand {
    position: absolute;
    left: 901px;
    top: 34px;
    width: 124px;
    height: 304px;
    border-radius: 4px;
    background: linear-gradient(180deg, var(--display-light), var(--display-shade));
  }
  .cover-actions {
    position: absolute;
    top: 338px;
    left: 722px;
    display: flex;
    gap: 18px;
    font-family: "Roboto", sans-serif;
    font-weight: 500;
    font-size: 15px;
    color: var(--button-text);
  }
  .action-button,
  .action-group {
    height: 33px;
    background: var(--white);
    border: 1px solid var(--button-border);
    border-radius: 2px;
    display: flex;
    align-items: center;
  }
  .action-button { padding: 0 12px; }
  .action-group .action-part { padding: 0 12px; height: 100%; display: flex; align-items: center; }
  .action-group .action-part + .action-part { border-left: 1px solid var(--button-border); }
  .dots { display: flex; gap: 4px; }
  .dots span { width: 4px; height: 4px; border-radius: 50%; background: var(--button-text); }
  .avatar {
    position: absolute;
    left: 20px;
    top: 214px;
    width: 210px;
    height: 210px;
    background: var(--white);
    padding: 5px;
    z-index: 2;
  }
  .avatar-fill { width: 100%; height: 100%; background: var(--avatar-fill); }
  .tab-bar {
    position: absolute;
    left: 250px;
    top: 394px;
    height: 52px;
    display: flex;
    font-family: "Roboto", sans-serif;
    font-weight: 500;
    font-size: 18px;
  }
  .tab {
    position: relative;
    display: flex;
    align-items: center;
    justify-content: center;
    height: 100%;
    color: var(--tab-link);
    border-left: 1px solid var(--tab-divider);
  }
  .tab-timeline { width: 115px; color: var(--tab-active); }
  .tab-about { width: 94px; }
  .tab-friends { width: 107px; }
  .tab-photos { width: 102px; }
  .tab-more { width: 100px; gap: 10px; }
  .tab-timeline::after {
    content: "";
    position: absolute;
    bottom: 0;
    left: 50%;
    margin-left: -9px;
    border: 9px solid transparent;
    border-bottom-color: var(--page-bg);
    border-top: 0;
  }
  .caret {
    border: 6px solid transparent;
    border-top: 6px solid var(--tab-link);
    border-bottom: 0;
  }
</style>
</head>
<body>
  <section class="profile-header">
    <div class="cover">
      <h1 class="headline">
        <span class="headline-main">Smartphone Accessories</span>
        <span class="headline-sub">Perfect for Queues and Checkouts</span>
      </h1>

      <div class="product-row">
        <div class="product" role="img" aria-label="Photo of a boxed audio cable"></div>
        <div class="product" role="img" aria-label="Photo of a boxed USB car adapter"></div>
        <div class="product" role="img" aria-label="Photo of a boxed phone charging cable"></div>
        <div class="product" role="img" aria-label="Photo of a boxed micro-USB cable"></div>
        <div class="product" role="img" aria-label="Photo of a boxed USB-C cable"></div>
        <div class="product" role="img" aria-label="Photo of a boxed USB wall adapter"></div>
      </div>

      <div class="display-stand" role="img" aria-label="Photo of a clear countertop display tower stocked with earbuds, charging cables and power adapters"></div>

      <div class="cover-actions">
        <div class="action-button">Update Info</div>
        <div class="action-group">
          <div class="action-part">View Activity Log</div>
          <div class="action-part"><span class="dots"><span></span><span></span><span></span></span></div>
        </div>
      </div>
    </div>

    <div class="avatar"><div class="avatar-fill"></div></div>

    <nav class="tab-bar">
      <div class="tab tab-timeline">Timeline</div>
      <div class="tab tab-about">About</div>
      <div class="tab tab-friends">Friends</div>
      <div class="tab tab-photos">Photos</div>
      <div class="tab tab-more">More <span class="caret"></span></div>
    </nav>
  </section>
</body>
</html>
```